Menu Board 1000mmx500mm re-design

I would like to re-design exiting menu board 1000mmx500mm. Current board letters are bit to small to read. I would like to have pictures (attached) of the food offered on it and at the same time to create balance between pictures and size of the text to be easily readable. Fonts and colours are up to designer choice but prefer warm and bright colours rather anything dark.

Target Market(s)

Food industry

Industry/Entity Type

Food

Font styles to use
Other font styles liked:
• I leave font choice to designer

Colors
FFC000
F8CF3A
FAE287
FDF2CF
FEFAEE
F0912C
F2A743
F7CA91
FBE8D2
FDF5EE
EE7325
F08F49
F5BC92
FAE3D3
FDF4ED

Requirements
Must have
• Pictures + Text
Nice to have
• Balance between images and text.
Should not have
• Can't think of any

```html
<!DOCTYPE html>
<html lang="en">
<head>
<meta charset="utf-8">
<title>Menu Board</title>
<link href="https://fonts.googleapis.com/css2?family=Josefin+Sans:wght@700&family=Russo+One&family=Nunito:wght@700&display=swap" rel="stylesheet">
<style>
  :root {
    --bg: #f3efe6;
    --board-top: #fefaee;
    --board-bottom: #fbe8d2;
    --yellow: #ffc000;
    --yellow-warm: #f8bf22;
    --orange: #ee7325;
    --orange-soft: #f0912c;
    --white: #ffffff;
    --ink: #2b1a0e;
    --text: #3a2614;
    --photo-warm: #c98a3a;
    --photo-bread: #e8c07a;
    --photo-green: #5d7a3a;
    --photo-roast: #b8642a;
    --photo-chicken: #9a5a2a;
  }
  * { margin: 0; padding: 0; box-sizing: border-box; }
  html, body { width: 1200px; height: 800px; overflow: hidden; background: var(--bg); }
  .board {
    position: absolute; left: 420px; top: 16px; width: 360px; height: 768px;
    background: linear-gradient(180deg, var(--board-top), var(--board-bottom));
    overflow: hidden;
  }
  .photo-cluster { position: absolute; left: 0; top: 0; width: 360px; height: 290px; }
  .brush { position: absolute; }
  .title {
    position: absolute; left: 0; width: 100%; text-align: center;
    font-family: 'Josefin Sans', sans-serif; font-weight: 700; color: var(--white);
    text-shadow: -3px 2px 0 var(--ink);
  }
  .title--menu { top: 290px; font-size: 60px; letter-spacing: 1px; }
  .title--sauces {
    top: 600px; font-size: 32px;
    font-family: 'Russo One', sans-serif; text-shadow: -2px 2px 0 var(--ink);
  }
  .menu-col { position: absolute; top: 378px; }
  .menu-col--left { left: 9px; width: 160px; }
  .menu-col--right { left: 180px; width: 173px; }
  .item { margin-bottom: 10px; }
  .item__head {
    display: flex; align-items: baseline;
    font-family: 'Russo One', sans-serif; font-size: 12.5px; color: var(--orange);
  }
  .item__head::before {
    content: ""; width: 4px; height: 4px; border-radius: 50%;
    background: var(--orange-soft); margin-right: 4px; align-self: center;
  }
  .item__leader { flex: 1; border-bottom: 1.5px dotted var(--orange); margin: 0 2px; transform: translateY(-3px); min-width: 6px; }
  .item__desc {
    font-family: 'Nunito', sans-serif; font-weight: 700; font-size: 8.8px; line-height: 1.3;
    color: var(--text); padding-left: 8px; margin-top: 2px;
  }
  .sauce {
    position: absolute; font-family: 'Russo One', sans-serif; font-size: 15px;
    color: var(--white); text-shadow: -1.5px 1.5px 0 var(--ink);
    display: flex; align-items: center; white-space: nowrap;
  }
  .sauce::before {
    content: ""; width: 6px; height: 6px; border-radius: 50%;
    background: var(--ink); margin-right: 5px;
  }
</style>
</head>
<body>
<main class="board">
  <svg class="photo-cluster" viewBox="0 0 360 290" width="360" height="290">
    <circle cx="241" cy="135" r="134" fill="var(--yellow)"/>
    <circle cx="241" cy="135" r="129" fill="var(--photo-warm)" role="img" aria-label="Photo of a grilled chicken wrap cut in half"/>
    <circle cx="99" cy="77" r="36" fill="var(--white)"/>
    <circle cx="99" cy="77" r="34" fill="var(--photo-roast)" role="img" aria-label="Photo of roasted potatoes"/>
    <circle cx="99" cy="155" r="38" fill="var(--yellow)"/>
    <circle cx="99" cy="155" r="36" fill="var(--photo-bread)" role="img" aria-label="Photo of a chicken ciabatta"/>
    <circle cx="146" cy="214" r="36" fill="var(--white)"/>
    <circle cx="146" cy="214" r="34" fill="var(--photo-green)" role="img" aria-label="Photo of a beetroot wrap"/>
    <circle cx="222" cy="230" r="37" fill="var(--yellow)"/>
    <circle cx="222" cy="230" r="35" fill="var(--photo-roast)" role="img" aria-label="Photo of potatoes with thyme"/>
    <circle cx="301" cy="218" r="38" fill="var(--yellow)"/>
    <circle cx="301" cy="218" r="36" fill="var(--photo-chicken)" role="img" aria-label="Photo of roast chicken with veggie rice"/>
  </svg>

  <svg class="brush" style="left:14px;top:272px" width="330" height="96" viewBox="0 0 330 96">
    <path d="M40 8 L300 4 L296 14 L318 16 L300 26 L326 34 L304 44 L322 56 L298 64 L312 74 L280 82 L240 90 L150 92 L70 86 L30 80 L46 70 L6 62 L36 54 L2 46 L30 36 L12 26 L36 18 Z" fill="var(--yellow-warm)"/>
  </svg>
  <h1 class="title title--menu">MENU</h1>

  <section class="menu-col menu-col--left">
    <div class="item">
      <div class="item__head">CIABATTA<span class="item__leader"></span>£6</div>
      <p class="item__desc">Roti Chicken, Rucola, Caramelized<br>Onions, Tomato, Fresh Onion</p>
    </div>
    <div class="item">
      <div class="item__head">WRAP<span class="item__leader"></span>£7</div>
      <p class="item__desc">Roti Chicken, Cruncgy Slaw,<br>Tomato, Fresh Onion &amp; Sauce of<br>your choice</p>
    </div>
    <div class="item">
      <div class="item__head">BEETROOT WRAP<span class="item__leader"></span>£8</div>
      <p class="item__desc">Roti Chicken, Cruncgy Slaw,<br>Tomato, Fresh Onion &amp; Sauce of<br>your choice</p>
    </div>
  </section>

  <section class="menu-col menu-col--right">
    <div class="item">
      <div class="item__head">1/4 CHICKEN BOX<span class="item__leader"></span>£9</div>
      <p class="item__desc">Roti Chicken, Veggie Rice &amp; Salad</p>
    </div>
    <div class="item">
      <div class="item__head">1/2 CHICKEN BOX<span class="item__leader"></span>£14</div>
      <p class="item__desc">Roti Chicken, Veggie Rice &amp; Salad</p>
    </div>
    <div class="item">
      <div class="item__head">ROASTED POTAOES<span class="item__leader"></span>£2.5</div>
      <p class="item__desc">Thyme &amp; Garlic</p>
    </div>
    <div class="item">
      <div class="item__head">WATER<span class="item__leader"></span>£1</div>
    </div>
    <div class="item">
      <div class="item__head">CAN &amp; JUICES<span class="item__leader"></span>£1.8</div>
    </div>
  </section>

  <svg class="brush" style="left:30px;top:576px" width="306" height="180" viewBox="0 0 306 180">
    <path d="M14 6 L250 2 L270 10 L262 22 L284 34 L272 48 L290 62 L280 80 L300 96 L282 110 L298 122 L280 140 L292 156 L260 166 L200 176 L90 174 L30 168 L12 152 L24 138 L2 124 L20 108 L6 92 L24 76 L10 58 L26 42 L8 24 Z" fill="var(--yellow-warm)"/>
  </svg>
  <h2 class="title title--sauces">SAUCES</h2>
  <span class="sauce" style="left:58px;top:654px">SIGNATURE</span>
  <span class="sauce" style="left:218px;top:654px">PIRI PIRI</span>
  <span class="sauce" style="left:156px;top:676px">BBQ</span>
  <span class="sauce" style="left:45px;top:700px">SWEET CHILLI</span>
  <span class="sauce" style="left:200px;top:700px">GARLIC MAYO</span>
</main>
</body>
</html>
```